Visitenkarten-Design für Persisches Restaurant
Zielgruppe
persisches Restaurant, suche ein Hochwertiges Design für internationale Kunden
Aufgabenstellung
möchte eine hochwertige und elegante visitenkarte
auf der Vorderseite sollte das Logo sein und auf der Rückseite Öffnungszeit, Adresse, Tel. E-Mail und homepage

```html
<!DOCTYPE html>
<html lang="de">
<head>
<meta charset="utf-8">
<title>Darvana – Visitenkarte</title>
<link href="https://fonts.googleapis.com/css2?family=Montserrat:wght@400;600&display=swap" rel="stylesheet">
<style>
  :root {
    --stage: #e6e6e6;
    --brown: #4d3327;
    --gold: #c9a145;
    --paper: #f2f2f1;
    --ink: #1c1c1c;
    --shadow: rgba(0,0,0,0.18);
  }
  * { margin: 0; padding: 0; box-sizing: border-box; }
  html, body { width: 1200px; height: 1200px; overflow: hidden; }
  body {
    background: var(--stage);
    font-family: "Montserrat", sans-serif;
    position: relative;
  }
  .card {
    position: absolute;
    left: 170px;
    width: 860px;
    height: 520px;
    box-shadow: 0 10px 30px var(--shadow);
  }
  .card--front { top: 50px; background: var(--brown); }
  .card--back { top: 630px; background: var(--paper); color: var(--ink); }

  .brand {
    position: absolute;
    text-align: center;
    font-weight: 600;
  }
  .card--front .brand {
    left: 0; right: 0; top: 175px;
    color: var(--gold);
  }
  .brand__name { font-size: 86px; letter-spacing: 6px; line-height: 1; }
  .brand__tagline { font-size: 17px; letter-spacing: 5px; margin-top: 12px; font-weight: 400; }
  .brand__since { font-size: 11px; letter-spacing: 3px; margin-top: 6px; font-weight: 400; }
  .brand__rule { width: 330px; height: 1.5px; background: currentColor; margin: 8px auto 0; }

  .card--back .brand {
    left: 60px; top: 56px;
    color: var(--ink);
    text-align: left;
  }
  .card--back .brand__name { font-size: 46px; letter-spacing: 3px; }
  .card--back .brand__tagline { font-size: 10px; letter-spacing: 3px; margin-top: 8px; }
  .card--back .brand__since { font-size: 7px; letter-spacing: 2px; margin-top: 4px; text-align: center; }
  .card--back .brand__rule { width: 100%; height: 1px; margin: 5px 0 0; }

  .details {
    position: absolute;
    left: 330px; top: 210px;
    width: 470px;
  }
  .details__block {
    border-bottom: 2.5px solid var(--ink);
    padding-bottom: 10px;
    margin-bottom: 16px;
  }
  .person__name { font-size: 30px; font-weight: 600; line-height: 1.1; }
  .person__role { font-size: 24px; font-weight: 400; }
  .address { font-size: 19px; line-height: 1.35; }
  .contact { list-style: none; font-size: 19px; line-height: 1.45; }
  .contact li { display: flex; align-items: center; gap: 10px; }
  .contact svg { width: 18px; height: 18px; flex: none; }
</style>
</head>
<body>
  <section class="card card--front" aria-label="Vorderseite">
    <div class="brand">
      <div class="brand__name">DARVANA</div>
      <div class="brand__tagline">PERSISCHES RESTAURANT</div>
      <div class="brand__since">SINCE 1999</div>
      <div class="brand__rule"></div>
    </div>
  </section>

  <section class="card card--back" aria-label="Rückseite">
    <div class="brand">
      <div class="brand__name">DARVANA</div>
      <div class="brand__tagline">PERSISCHES RESTAURANT</div>
      <div class="brand__since">SINCE 1999</div>
      <div class="brand__rule"></div>
    </div>

    <div class="details">
      <div class="details__block person">
        <div class="person__name">Reza Amani</div>
        <div class="person__role">Manager</div>
      </div>
      <div class="details__block address">
        Lindenweg 14, 60431<br>
        Frankfurt am Main, Germany
      </div>
      <div class="details__block">
        <ul class="contact">
          <li>
            <svg viewBox="0 0 24 24" aria-hidden="true"><path d="M6.6 2.5l3 3-2 2.6c1.2 2.6 3.3 4.7 5.9 5.9l2.6-2 3 3-2.2 3.2C10.6 18.5 5.5 13.4 3.4 4.7z" fill="none" stroke="currentColor" stroke-width="1.8" stroke-linejoin="round"/></svg>
            +49 69 204816
          </li>
          <li>
            <svg viewBox="0 0 24 24" aria-hidden="true"><rect x="2.5" y="5" width="19" height="14" fill="none" stroke="currentColor" stroke-width="1.8"/><path d="M2.5 5l9.5 8 9.5-8M2.5 19l7-7M21.5 19l-7-7" fill="none" stroke="currentColor" stroke-width="1.6"/></svg>
            darvana-kueche.de
          </li>
        </ul>
      </div>
    </div>
  </section>
</body>
</html>
```